Wattlebrook Legal: Sole Practitioner Law Firm seeking corporate branding drawing on unique bush setting

I need a logo, stationary and business card design for my law firm. I will be practising as a sole practitioner specialising in corporate, commercial, finance, migration and agriculture law. Having left my corporate job in the city and relocated our family to our farm in regional Western Australia, I would like the corporate design for my company to be crisp, stylish, concise and uncomplicated. The law firm is called "Wattlebrook Legal" because we have a colony of the endangered Carnaby Black Cockatoos living in the bush behind our homestead (which is also my office). I will travel to clients rather than have them visit me. I would like to see a stylised image of the bird with some Australian native bush included in the design, either as a background image on the back of the card. A separate brief has been created for the logo and stationary though I hope all 3 pieces of work will "marry". The final design should communicate clarity of vision, efficiency, compassion and solution/ outcome focused. I prefer to have the business cards printed on card with a bit of texture and substance. I will try not to use laminated card as I consider it feels "plastic and commoditised" which is inconsistent with the image and feel of the business I intend creating. Please see attached brief for further details of the design brief.

Target Market(s)

Agriculture and Horticulture companies, Farmers, Family offices and estates, banks, insurance companies, individuals wishing to migrate to Australia

Industry/Entity Type

Legal

Contact Information for Business Card

Harriet Lyle-Pemberton
LLB (Hons), BSc., MEc.
Legal Practitioner and Director

WATTLEBROOK LEGAL PTY LTD
PO Box 726, Kerrawind WA 6091
Ph: 0452 781906
Email: harrietlp@ferncastmail.com

Solicitor admitted to practice in the Upper Bench of Kestrel Shore, England and Wales, NSW, and Registered Practitioner of the Chief Bench of Marrowdale

Logo Text

WATTLEBROOK LEGAL: Client Focused Commercial Legal Solutions

Font styles to use
Other font styles liked:
• Verlag

Colors
ec1f27
fbee3d
9bcb3c
ffffff
1b1b1b
c4c4c4

Requirements
Must have
• A look and feel of quality, conservatism, adventure
Nice to have
• A stylised image of a Carnaby Cockatoo and Australian flora as a background image or design on the back of the card.
Should not have
• Clutter, cartoons

```html
<!DOCTYPE html>
<html lang="en">
<head>
<meta charset="utf-8">
<title>Wattlebrook Legal – Business Card Options</title>
<link rel="stylesheet" href="https://fonts.googleapis.com/css2?family=Oswald:wght@300;400;500&family=Raleway:wght@400&family=Bungee&display=swap">
<style>
  :root {
    --bg-light: #d9d9d9;
    --bg-dark: #a3a3a3;
    --card: #f4f4f4;
    --ink: #1b1b1b;
    --ink-soft: #555555;
    --red: #c2281f;
    --band-dark: #3a3a3a;
    --band-grey: #c4c4c4;
    --dome: #c9c9c9;
    --accent-edge: #e0531f;
    --white: #ffffff;
  }
  * { margin: 0; padding: 0; box-sizing: border-box; }
  html, body { width: 1200px; height: 834px; overflow: hidden; }
  body {
    position: relative;
    background: radial-gradient(ellipse at 50% 35%, var(--bg-light) 0%, var(--bg-dark) 100%);
    font-family: "Oswald", sans-serif;
  }

  .card {
    position: absolute;
    width: 410px;
    height: 232px;
    background: var(--card);
    box-shadow: 0 4px 8px rgba(0,0,0,0.35);
    overflow: hidden;
  }
  .card svg.card-shapes { position: absolute; inset: 0; }

  .option-number {
    position: absolute;
    font-family: "Bungee", sans-serif;
    font-size: 44px;
    line-height: 1;
    color: var(--ink);
  }

  /* Back of card */
  .card-back { left: 384px; top: 36px; width: 430px; height: 240px; background: var(--white); }
  .card-back .bush-art { position: absolute; left: 0; top: 0; width: 430px; height: 176px; }
  .card-back .emblem {
    position: absolute; left: 115px; top: 22px; width: 200px; height: 200px;
    border-radius: 50%; background: var(--white);
  }
  .card-back .firm-name {
    position: absolute; left: 0; width: 430px; top: 112px; text-align: center;
    font-family: "Raleway", sans-serif; font-size: 30px; color: var(--ink); letter-spacing: -0.5px;
  }
  .card-back .firm-rule {
    position: absolute; left: 170px; width: 90px; top: 160px; border-top: 1px solid #bbb;
  }
  .card-back .admission {
    position: absolute; left: 0; width: 430px; top: 190px; text-align: center;
    font-family: "Raleway", sans-serif; font-size: 9.6px; line-height: 16px; color: var(--ink);
    letter-spacing: -0.1px; white-space: nowrap;
  }

  /* Front of card */
  .brand-mark {
    position: absolute; left: 0; width: 100%; top: 30px; text-align: center;
    font-family: "Oswald", sans-serif; font-weight: 400; font-size: 17px; color: var(--ink);
    letter-spacing: 1px;
  }
  .rule { position: absolute; left: 145px; width: 120px; border-top: 1px solid #9a9a9a; }
  .holder-name {
    position: absolute; left: 0; width: 100%; top: 76px; text-align: center;
    font-weight: 400; font-size: 21px; letter-spacing: 0.2px; text-transform: uppercase;
  }
  .credentials {
    position: absolute; left: 0; width: 100%; top: 106px; text-align: center;
    font-weight: 400; font-size: 11px; letter-spacing: 3px; color: var(--ink);
  }
  .position-title {
    position: absolute; left: 0; width: 100%; top: 122px; text-align: center;
    font-weight: 400; font-size: 9px; letter-spacing: 2.6px; color: var(--ink);
  }
  .address, .contact {
    position: absolute; font-weight: 300; font-size: 14px; line-height: 21px; text-transform: uppercase;
    white-space: nowrap;
  }
  .address { left: 22px; }
  .contact { right: 22px; text-align: right; }

  .name-red { color: var(--red); }
  .name-grey { color: var(--ink-soft); }
  .on-dark { color: var(--white); }
  .on-grey { color: var(--white); }

  .card-one { left: 108px; top: 292px; }
  .card-two { left: 94px; top: 550px; }
  .card-three { left: 680px; top: 300px; }
  .card-four { left: 644px; top: 562px; }
</style>
</head>
<body>

  <!-- Back of card -->
  <section class="card card-back">
    <svg class="bush-art" viewBox="0 0 430 176" role="img" aria-label="Illustration of black cockatoos perched among red, green and orange native bush foliage">
      <defs>
        <linearGradient id="bush" x1="0" y1="0" x2="1" y2="1">
          <stop offset="0" stop-color="#9bcb3c"/>
          <stop offset="0.45" stop-color="#d9463a"/>
          <stop offset="1" stop-color="#5f8f2e"/>
        </linearGradient>
      </defs>
      <rect width="430" height="176" fill="url(#bush)"/>
    </svg>
    <div class="emblem"></div>
    <div class="firm-name">Wattlebrook Legal</div>
    <div class="firm-rule"></div>
    <p class="admission">Solicitor admitted to practice in the Upper Bench of Kestrel Shore,<br>England and Wales, NSW, and Registered Practitioner of the Chief Bench of Marrowdale</p>
  </section>

  <!-- Option 1 -->
  <span class="option-number" style="left:66px; top:368px;">1</span>
  <section class="card card-one">
    <svg class="card-shapes" viewBox="0 0 410 232" width="410" height="232">
      <path d="M0,150 L103,150 A109,109 0 1 1 313,150 L410,150 L410,232 L0,232 Z" fill="var(--dome)"/>
      <path d="M103,150 A109,109 0 1 1 313,150" fill="none" stroke="#555" stroke-width="1.5"/>
      <rect x="0" y="228" width="410" height="4" fill="var(--accent-edge)"/>
    </svg>
    <div class="brand-mark">Wattlebrook Legal</div>
    <div class="holder-name name-red">Harriet Lyle-Pemberton</div>
    <div class="credentials">LLB (HONS), BSC., MEC.</div>
    <div class="position-title">LEGAL PRACTITIONER AND DIRECTOR</div>
    <div class="rule" style="top:142px;"></div>
    <div class="address on-grey" style="top:170px;">Wattlebrook Legal Pty Ltd<br>PO Box 726, Kerrawind WA 6091</div>
    <div class="contact on-grey" style="top:176px;">harrietlp@ferncastmail.com<br>0452 781906</div>
  </section>

  <!-- Option 2 -->
  <span class="option-number" style="left:52px; top:630px;">2</span>
  <section class="card card-two">
    <svg class="card-shapes" viewBox="0 0 410 232" width="410" height="232">
      <rect x="0" y="152" width="410" height="80" fill="var(--band-dark)"/>
      <rect x="0" y="150" width="410" height="2" fill="#cfcfcf"/>
    </svg>
    <div class="brand-mark">Wattlebrook Legal</div>
    <div class="rule" style="top:66px;"></div>
    <div class="holder-name name-grey">Harriet Lyle-Pemberton</div>
    <div class="credentials">LLB (HONS), BSC., MEC.</div>
    <div class="position-title">LEGAL PRACTITIONER AND DIRECTOR</div>
    <div class="rule" style="top:140px;"></div>
    <div class="address on-dark" style="top:170px;">Wattlebrook Legal Pty Ltd<br>PO Box 726, Kerrawind WA 6091</div>
    <div class="contact on-dark" style="top:176px;">harrietlp@ferncastmail.com<br>0452 781906</div>
  </section>

  <!-- Option 3 -->
  <span class="option-number" style="left:1108px; top:404px;">3</span>
  <section class="card card-three">
    <svg class="card-shapes" viewBox="0 0 410 232" width="410" height="232">
      <rect x="0" y="158" width="410" height="74" fill="var(--band-dark)"/>
      <rect x="0" y="155" width="410" height="3" fill="#cfcfcf"/>
    </svg>
    <div class="brand-mark">Wattlebrook Legal</div>
    <div class="rule" style="top:66px;"></div>
    <div class="holder-name name-red">Harriet Lyle-Pemberton</div>
    <div class="credentials">LLB (HONS), BSC., MEC.</div>
    <div class="position-title">LEGAL PRACTITIONER AND DIRECTOR</div>
    <div class="rule" style="top:140px;"></div>
    <div class="address on-dark" style="top:172px;">Wattlebrook Legal Pty Ltd<br>PO Box 726, Kerrawind WA 6091</div>
    <div class="contact on-dark" style="top:178px;">harrietlp@ferncastmail.com<br>0452 781906</div>
  </section>

  <!-- Option 4 -->
  <span class="option-number" style="left:1088px; top:664px;">4</span>
  <section class="card card-four">
    <svg class="card-shapes" viewBox="0 0 410 232" width="410" height="232">
      <rect x="0" y="154" width="410" height="78" fill="var(--band-grey)"/>
      <rect x="0" y="151" width="410" height="3" fill="var(--band-dark)"/>
      <rect x="0" y="227" width="410" height="5" fill="var(--band-dark)"/>
    </svg>
    <div class="brand-mark">Wattlebrook Legal</div>
    <div class="rule" style="top:66px;"></div>
    <div class="holder-name name-grey">Harriet Lyle-Pemberton</div>
    <div class="credentials">LLB (HONS), BSC., MEC.</div>
    <div class="position-title">LEGAL PRACTITIONER AND DIRECTOR</div>
    <div class="rule" style="top:140px;"></div>
    <div class="address on-grey" style="top:168px;">Wattlebrook Legal Pty Ltd<br>PO Box 726, Kerrawind WA 6091</div>
    <div class="contact on-grey" style="top:174px;">harrietlp@ferncastmail.com<br>0452 781906</div>
  </section>

</body>
</html>
```